V9 Web Design Project

New company website for Intel cyber security company.

Style should be cool, but remain appropriate for very serious subject matter and audience.

Target Market(s)

Target audience is government and the military

Navigation needs to include:
- About Us
- Services
- Careers
- Contact Us
- Contracts

As well as 2 feature areas - use "Technology Integration" and "Case Study" as the supporting headlines.

Industry/Entity Type

Security

Font styles to use
Sans Serif

Colors

Designer to choose colors to be used in the design.

Requirements
Must have
• Mountain imagery and theme.

Use logo attached.

New Tagline - "Securing the Continuum"
Nice to have
• Supporting imagery could include photos representative of security - avoid cliches.
Should not have
• Needs to be serious not frivolous

```html
<!DOCTYPE html>
<html lang="en">
<head>
<meta charset="utf-8">
<title>V9 Group — Securing the Continuum</title>
<link rel="stylesheet" href="https://fonts.googleapis.com/css2?family=Open+Sans:ital,wght@0,300;0,400;0,600;0,700;1,400&family=Questrial&display=swap">
<style>
:root{
  --ink:#1f1f24;
  --navy:#1b2a6b;
  --blue:#2b7fb8;
  --link:#2a9ad6;
  --grey:#707070;
  --sand:#ecebe4;
  --mist:#f6f6f6;
  --footer:#3f7ba1;
  --white:#ffffff;
  --sky:#3d6fb4;
  --snow:#eef2f6;
  --rock:#6f7f92;
}
*{margin:0;padding:0;box-sizing:border-box}
html,body{width:1200px;height:2376px;overflow:hidden;background:var(--white)}
body{position:relative;font-family:"Open Sans",Arial,sans-serif;color:var(--ink)}
.abs{position:absolute}

.site-header{position:absolute;left:0;top:0;width:1200px;height:56px;background:var(--white)}
.brand{position:absolute;left:98px;top:10px;display:flex;align-items:center;gap:10px}
.brand-mark{width:46px;height:38px;background:var(--navy)}
.brand-name{font-family:"Questrial",sans-serif;font-size:28px;color:var(--navy);letter-spacing:.5px}
.main-nav a{position:absolute;top:19px;font-size:14px;font-weight:700;color:var(--ink);text-decoration:none;letter-spacing:.3px}

.hero{left:0;top:56px;width:1200px;height:508px;
  background:
    radial-gradient(ellipse 420px 300px at 640px 330px,rgba(238,242,246,.95) 0%,rgba(238,242,246,0) 100%),
    radial-gradient(ellipse 380px 240px at 200px 420px,rgba(111,127,146,.55) 0%,rgba(111,127,146,0) 100%),
    radial-gradient(ellipse 360px 220px at 1040px 430px,rgba(111,127,146,.45) 0%,rgba(111,127,146,0) 100%),
    linear-gradient(180deg,var(--sky) 0%,#5f8fcb 28%,#b9cbe0 52%,var(--snow) 72%,#c3ced9 100%)}
.hero-title{left:0;top:264px;width:1200px;text-align:center;font-family:"Questrial",sans-serif;font-size:48px;font-weight:400;color:var(--white);letter-spacing:.5px}

.intro-heading{left:0;top:606px;width:1200px;text-align:center;font-family:"Questrial",sans-serif;font-size:33px;font-weight:400;color:var(--blue)}
.intro-text{left:205px;top:662px;width:790px;text-align:center;font-size:22px;font-weight:300;line-height:30px;color:var(--grey);letter-spacing:1.5px}
.btn{display:flex;align-items:center;justify-content:center;border:2px solid var(--blue);border-radius:4px;color:var(--navy);font-size:13px;text-decoration:none;background:var(--white)}
.intro-btn{left:523px;top:788px;width:154px;height:48px}

.feature-title{left:113px;top:958px;font-family:"Questrial",sans-serif;font-size:32px;font-weight:400;color:var(--ink)}
.feature-text{left:113px;top:1026px;width:490px;font-size:14px;line-height:24.2px;color:var(--ink)}
.feature-btn{left:113px;top:1208px;width:156px;height:48px}
.feature-image{left:669px;top:903px;width:384px;height:384px;background:radial-gradient(circle at 50% 45%,#d9d9d9 0%,#ededed 45%,#f7f7f7 100%)}

.case-band{left:0;top:1342px;width:1200px;height:444px;background:var(--sand)}
.case-title{left:0;top:1384px;width:1200px;text-align:center;font-family:"Questrial",sans-serif;font-size:32px;font-weight:400;color:var(--blue)}
.case-title b{font-family:"Open Sans",sans-serif;font-weight:700;font-size:30px}
.case-rule{left:586px;top:1440px;width:32px;height:4px;background:var(--grey)}
.case-card{top:1489px;width:231px;height:297px;background:var(--white);overflow:hidden}
.case-photo{width:231px;height:148px}
.case-card h3{margin:18px 14px 0 16px;font-size:17px;font-weight:400;line-height:20px;color:var(--ink)}
.case-card p{margin:12px 14px 0 16px;font-size:12px;line-height:17.5px;color:var(--ink)}

.voices{left:0;top:1830px;width:1200px;height:298px;background:var(--mist)}
.voice{top:1877px;width:300px}
.avatar{position:absolute;left:0;top:0;width:60px;height:60px;border-radius:50%;background:linear-gradient(160deg,#c9a48a,#8a6a55)}
.voice-text{position:absolute;left:69px;top:2px;width:218px;font-size:12px;line-height:19px;color:var(--ink)}
.voice-name{position:absolute;left:69px;top:148px;font-size:15px;font-weight:600;color:var(--ink);letter-spacing:.5px}
.voice-role{position:absolute;left:69px;top:188px;font-size:11px;font-style:italic;color:var(--ink)}
.voice-role span{color:var(--link);font-style:normal}

.site-footer{left:0;top:2168px;width:1200px;height:208px;background:var(--footer);color:var(--white)}
.footer-label{position:absolute;top:40px;font-size:15px}
.footer-line{position:absolute;font-size:13px;line-height:21px;color:#d6e4ee}
.footer-phone{position:absolute;font-size:16px;color:#e6eff5}
.social{position:absolute;left:566px;top:44px;display:flex;gap:8px}
.social a{width:40px;height:40px;border-radius:50%;background:var(--white);color:var(--footer);font-size:15px;font-weight:700;display:flex;align-items:center;justify-content:center;text-decoration:none}
.legal{position:absolute;left:97px;top:166px;font-size:12px}
</style>
</head>
<body>

<header class="site-header">
  <div class="brand"><span class="brand-mark"></span><span class="brand-name">V9 GROUP</span></div>
  <nav class="main-nav">
    <a style="left:499px">HOME</a>
    <a style="left:574px">ABOUT US</a>
    <a style="left:683px">SERVICES</a>
    <a style="left:786px">CAREERS</a>
    <a style="left:883px">CONTACT US</a>
    <a style="left:1008px">CONTRACTS</a>
  </nav>
</header>

<section class="abs hero" role="img" aria-label="Photograph of a snow-covered Himalayan mountain peak rising into a deep blue sky, with clouds around its base"></section>
<h1 class="abs hero-title">Securing the Continuum</h1>

<h2 class="abs intro-heading">V9 Group helps clients achieve new heights.</h2>
<p class="abs intro-text">V9 Group, Inc. is an independent consulting firm providing professional, technical and management solutions to leading global corporations and the federal government.</p>
<a class="abs btn intro-btn">READ MORE</a>

<h2 class="abs feature-title">Technology Integration Solutions</h2>
<p class="abs feature-text">V9 Group provides scientific, engineering, administrative, technical operational and analytical support services to federal and military clients with emerging technologies relating to operational needs. V9 Group works closely with our clients to deliver innovative technology integration solutions. We support critical networks and systems that require secure, reliable solutions.</p>
<a class="abs btn feature-btn">READ MORE</a>
<div class="abs feature-image" role="img" aria-label="Pencil sketch of a light bulb filled with gears, drawn by a hand"></div>

<section class="abs case-band"></section>
<h2 class="abs case-title"><b>Case</b> Study</h2>
<div class="abs case-rule"></div>

<article class="abs case-card" style="left:137px">
  <div class="case-photo" role="img" aria-label="Business team reviewing documents" style="background:linear-gradient(135deg,#8a7a70,#3c4048)"></div>
  <h3>Lorem ipsum dolor sit amet, adipiscing elit,</h3>
  <p>Lorem ipsum dolor sit amet, consectetur adipiscing elit, sed do eiusmod tempor incididunt ut labore et dolore magna aliqua. Ut</p>
</article>
<article class="abs case-card" style="left:368px">
  <div class="case-photo" role="img" aria-label="Office desk with glasses and colleagues by a window" style="background:linear-gradient(135deg,#e4e8ec,#9aa4ae)"></div>
  <h3>Lorem ipsum dolor sit amet, adipiscing elit,</h3>
  <p>Lorem ipsum dolor sit amet, consectetur adipiscing elit, sed do eiusmod tempor incididunt ut labore et dolore magna aliqua. Ut</p>
</article>
<article class="abs case-card" style="left:599px">
  <div class="case-photo" role="img" aria-label="Two colleagues working together at a tablet" style="background:linear-gradient(135deg,#c8ccd2,#5f7894)"></div>
  <h3>Lorem ipsum dolor sit amet, adipiscing elit,</h3>
  <p>Lorem ipsum dolor sit amet, consectetur adipiscing elit, sed do eiusmod tempor incididunt ut labore et dolore magna aliqua. Ut</p>
</article>
<article class="abs case-card" style="left:830px">
  <div class="case-photo" role="img" aria-label="Hands typing on a laptop at a bright desk" style="background:linear-gradient(135deg,#d8b068,#e8ecef)"></div>
  <h3>Lorem ipsum dolor sit amet, adipiscing elit,</h3>
  <p>Lorem ipsum dolor sit amet, consectetur adipiscing elit, sed do eiusmod tempor incididunt ut labore et dolore magna aliqua. Ut</p>
</article>

<section class="abs voices"></section>
<div class="abs voice" style="left:117px">
  <div class="avatar" role="img" aria-label="Portrait photo of the client"></div>
  <p class="voice-text">Lorem ipsum dolor sit amet, consectetur adipiscing elit, sed do eiusmod tempor incididunt ut labore et dolore magna aliqua. Ut enim ad minim veniam, quis nostrud exercitation ullamco laboris nisi ut aliquip ex ea commodo consequat.</p>
  <div class="voice-name">Name</div>
  <div class="voice-role">President, <span>Company Name</span></div>
</div>
<div class="abs voice" style="left:447px">
  <div class="avatar" role="img" aria-label="Portrait photo of the client"></div>
  <p class="voice-text">Lorem ipsum dolor sit amet, consectetur adipiscing elit, sed do eiusmod tempor incididunt ut labore et dolore magna aliqua. Ut enim ad minim veniam, quis nostrud exercitation ullamco laboris nisi ut aliquip ex ea commodo consequat.</p>
  <div class="voice-name">Name</div>
  <div class="voice-role">President, <span>Company Name</span></div>
</div>
<div class="abs voice" style="left:782px">
  <div class="avatar" role="img" aria-label="Portrait photo of the client" style="background:linear-gradient(160deg,#b8917a,#3a2a24)"></div>
  <p class="voice-text">Lorem ipsum dolor sit amet, consectetur adipiscing elit, sed do eiusmod tempor incididunt ut labore et dolore magna aliqua. Ut enim ad minim veniam, quis nostrud exercitation ullamco laboris nisi ut aliquip ex ea commodo consequat.</p>
  <div class="voice-name">Name</div>
  <div class="voice-role">President, <span>Company Name</span></div>
</div>

<footer class="abs site-footer">
  <div class="footer-label" style="left:97px">Location</div>
  <div class="footer-line" style="left:97px;top:66px">Northern Virginia Location<br>4410 Ridgeline Avenue, Suite 120<br>Fairbrook, VA 22000</div>
  <div class="footer-label" style="left:370px">Connect with us</div>
  <div class="footer-line" style="left:370px;top:66px">contact@v9summitgroup.com</div>
  <div class="footer-phone" style="left:370px;top:88px">(555) 014-2070</div>
  <nav class="social" aria-label="Social links">
    <a aria-label="Pinecast">P</a>
    <a aria-label="Linkwell">L</a>
    <a aria-label="Nearby">N</a>
  </nav>
  <div class="legal">© 2014 V9 Group Inc. All Rights Reserved. &nbsp;|&nbsp; Terms of use &nbsp;|&nbsp; Privacy Policy</div>
</footer>

</body>
</html>
```